Women Web Portal

We are developing an internet portal with content created by and for women in Latin America.
This portal will contain different categories focused on relevant topics for women who are at the same time mothers, lovers, workers, pet-owners, ...

We are looking for design that are at the same time uncluttered, easy-to-use and obvious, and comfy. Pastel colours, buttons using traditional fonts, large space for pictures, highlighted social elements,...

Our target being the middle-class women, we want a design that feels comfortable, real, a bit trendy and traditional, not a Tarsk & Welmore design, something women can relate to and feel comfortable enough to come back and participate.

Examples of websites:
www.dishtable.example
mujer.qelvo.example
www.cabellorinva.example
www.fourneau.example
Updates

Hi dear designers. After viewing some first drafts, I have updated the brief so you might have a better understanding of what we are looking for.

Thanks

Reason: We've been away for a while, unavailable to provide adequate feedback to the designs already sent. So we're extending the deadline in order to give time to everyone to adapt their work according to the feedback we'll be providing today.

Target Market(s)

Women between 25 and 50 years from Latin America. Mainly mothers: basically, we want women to interact with each other and with the content of the site so they create a strong community.

Advertisingly speaking, we want to have users, contents and FMCG brands to live together on this website.

Industry/Entity Type

Internet

Requirements
Must have
• Pastel colours for category tabs. Comfortable look & feel.

The design should include 3 different pages:
- Homepage
- Article page
- User profile

The page will be done in responsive design, so design should be thought to be adapted according to the browser (2 or 3 columns).

Thanks for doing it as a PSD file .

The design should also include:
- 8 category tabs
- Space for 728x90px and 300x600px advertising format.
- A relevant menu bar at the beginning of each page
Nice to have
• News feed/best content/most active comments zone: we need to bring forward content to our users so they'll be attracted to visit more pages of the website.

Small format to register (account).

Slider or any other moving objects.

Any idea that would facilitate and increase user participation
Should not have
• Actual text. please use Lorem Ipsum.

```html
<!DOCTYPE html>
<html lang="es">
<head>
<meta charset="utf-8">
<title>ellavida.example</title>
<link href="https://fonts.googleapis.com/css2?family=Didact+Gothic&family=Arimo:wght@400;700&display=swap" rel="stylesheet">
<style>
:root{
  --pink:#e8457a;
  --pink-light:#f27ea3;
  --pink-dark:#d93a6d;
  --red:#d42a3f;
  --ink:#1f1f1f;
  --grey-text:#6b6b6b;
  --hero-bg:#efefef;
  --page-bg:#f4f4f4;
  --card-border:#dedede;
  --green:#9dbd6a;
  --blue:#27a8de;
  --olive:#4f5a1a;
}
*{box-sizing:border-box;margin:0;padding:0}
html,body{width:990px;height:1200px;overflow:hidden}
body{position:relative;background:var(--page-bg);font-family:"Arimo",Arial,sans-serif;color:var(--grey-text)}
.abs{position:absolute}
.heading{font-family:"Didact Gothic","Century Gothic",sans-serif}

/* header */
.site-header{left:0;top:0;width:990px;height:46px;background:linear-gradient(#fff,#f1f1f1)}
.brand{left:168px;top:10px;display:flex;align-items:center;gap:6px;font-family:"Didact Gothic",sans-serif;font-size:24px;color:var(--ink)}
.brand-dot{width:28px;height:28px;border-radius:50%;background:var(--pink)}
.btn-social{left:458px;top:12px;width:112px;height:20px;background:var(--blue);color:#fff;font-size:10px;text-align:center;line-height:20px;border-radius:2px}
.btn-login{left:578px;top:12px;width:52px;height:20px;background:var(--pink);color:#fff;font-size:10px;text-align:center;line-height:20px;border-radius:2px}
.search{left:640px;top:12px;width:184px;height:20px;background:#fff;border:1px solid #e2e2e2;font-size:9px;color:#999;line-height:18px;padding-left:10px}
.search-btn{right:-1px;top:-1px;width:21px;height:20px;background:var(--pink);border-radius:2px}

/* nav */
.main-nav{left:0;top:46px;width:990px;height:29px;background:linear-gradient(var(--pink-light),var(--pink-dark));border-bottom:2px solid #c9315f}
.main-nav ul{position:absolute;left:168px;top:0;width:656px;height:27px;display:flex;list-style:none}
.main-nav li{font-family:"Didact Gothic",sans-serif;color:#fff;font-size:9.5px;line-height:27px;padding:0 13px;border-right:1px solid rgba(0,0,0,.12);white-space:nowrap}
.main-nav li:first-child{padding-left:7px}
.main-nav li:last-child{border:none}

/* hero */
.hero{left:0;top:77px;width:990px;height:389px;background:var(--hero-bg);border-bottom:2px solid #dcdcdc}
.hero-photo{left:168px;top:88px;width:240px;height:378px;background:radial-gradient(ellipse at 50% 55%,#a9d3c2 0%,#b9c9dc 45%,#e9e1d8 75%,var(--hero-bg) 100%)}
.hero-copy{left:386px;top:206px}
.hero-copy .kicker{font-size:17px;color:var(--ink);letter-spacing:-.5px;margin-left:5px}
.hero-copy .title{font-size:35px;color:var(--pink);line-height:28px;letter-spacing:-1.5px}
.hero-copy .sub{font-size:20px;color:#e8a34d;line-height:20px;margin-left:84px;letter-spacing:-.5px}
.hero-copy p{font-size:9px;line-height:11px;margin:9px 0 0 2px;width:240px}
.btn-discover{display:inline-block;margin:9px 0 0 0;padding:3px 9px;background:linear-gradient(#8a8a8a,#5a5a5a);color:#fff;font-size:17px;letter-spacing:-.6px;border-radius:3px}

.date-panel{left:654px;top:77px;width:170px;height:343px;background:#fff;box-shadow:0 1px 3px rgba(0,0,0,.15)}
.date-panel .date{height:64px;border-bottom:1px solid #e6e6e6;padding:20px 0 0 13px;color:#000;font-size:28px;letter-spacing:-1px}
.date-panel .date b{font-weight:400;font-size:38px}
.date-panel .date small{font-size:13px}
.teaser{padding:10px 12px 0 12px;border-bottom:1px solid #eee}
.teaser h3{font-family:"Didact Gothic",sans-serif;font-weight:400;font-size:8.5px;color:var(--olive);margin-bottom:5px}
.teaser p{font-size:7px;line-height:10px;color:#777}

/* boxes */
.box{background:#fff;border:1px solid #e2e2e2;box-shadow:0 1px 2px rgba(0,0,0,.12)}
.badge{display:inline-block;width:16px;height:13px;background:var(--red);color:#fff;font-size:7px;text-align:center;line-height:13px;border-radius:2px;position:relative;vertical-align:middle}
.badge::after{content:"";position:absolute;left:3px;bottom:-3px;border:3px solid transparent;border-top-color:var(--red);border-left-color:var(--red)}
.meta{font-size:7.5px;color:var(--red)}

.feature{left:166px;top:477px;width:481px;height:115px;padding:10px 10px}
.feature h2{font-family:"Didact Gothic",sans-serif;font-weight:400;font-size:19px;color:var(--pink);padding-bottom:6px;border-bottom:1px solid #eee;letter-spacing:-.4px}
.feature h2 .badge{margin-right:4px}
.feature p{font-size:7.8px;line-height:12.5px;margin:8px 2px 9px}

.register{left:654px;top:477px;width:172px;height:115px;padding:10px 10px}
.panel-title{font-family:"Didact Gothic",sans-serif;font-weight:400;font-size:20px;color:var(--ink);letter-spacing:-.5px;padding-bottom:4px;border-bottom:1px solid #e4e4e4}
.register .field{margin-top:8px;height:20px;border:1px solid #ddd;font-size:8px;color:#999;line-height:18px;padding-left:5px}
.btn-register{margin:10px 0 0 70px;width:83px;height:20px;background:linear-gradient(var(--pink-light),var(--pink-dark));color:#fff;font-size:8px;line-height:20px;text-align:center;border-radius:3px}

.card{top:602px;width:157px;height:223px;padding:5px}
.card .photo{height:105px;border:3px solid var(--pink)}
.card h3{font-family:"Didact Gothic",sans-serif;font-weight:400;font-size:14px;color:var(--pink);margin:8px 0 10px 2px}
.card h3 .badge{margin-right:3px}
.card p{font-size:7px;line-height:10.5px;margin:0 4px 6px}
.card .meta{margin-left:2px}

.highlights{left:654px;top:602px;width:172px;height:223px;padding:9px 10px}
.hl-item{display:flex;gap:5px;margin-top:12px}
.hl-num{flex:none;width:23px;height:23px;background:#1e1e1e;color:#fff;font-size:10px;line-height:23px;text-align:center;border-radius:2px;position:relative}
.hl-num::after{content:"";position:absolute;left:2px;bottom:-4px;border:3px solid transparent;border-top-color:#1e1e1e;border-left-color:#1e1e1e}
.hl-item b{display:block;font-weight:400;font-size:8.5px;color:var(--pink)}
.hl-item span{font-size:7.5px}
.hl-more{font-size:7px;color:var(--red);margin:6px 0 0 28px}

.promo{left:166px;top:836px;width:480px;height:39px;background:linear-gradient(#b3d181,#8fb15b);border:1px solid #86a656;display:flex;align-items:center;padding-left:11px;color:#fff}
.promo .pct{font-size:27px;color:var(--ink);letter-spacing:-2px}
.promo .pct small{font-size:11px}
.promo .line{font-family:"Didact Gothic",sans-serif;font-size:12px;margin-left:8px}
.promo .line em{font-style:normal;font-size:19px}

.popular{left:166px;top:883px;width:481px;height:223px;padding:10px 10px}
.popular .panel-title{display:flex;align-items:center;gap:6px;border-bottom:1px solid #eee}
.pop-item{display:flex;gap:10px;padding:10px 4px 8px;border-bottom:1px solid #f0f0f0}
.pop-item:last-child{border:none}
.pop-thumb{flex:none;width:70px;height:66px;border:3px solid #f0f0f0}
.pop-item h4{font-family:"Didact Gothic",sans-serif;font-weight:400;font-size:13px;color:var(--pink);margin:0 0 6px}
.pop-item p{font-size:7px;line-height:10px}
.btn-more{display:inline-block;margin-top:6px;padding:3px 9px;border:1px solid #ccc;font-size:7px;color:#888;background:#f7f7f7}

.gallery{left:654px;top:836px;width:172px;height:270px;padding:10px 10px}
.gallery .arrows{position:absolute;right:8px;top:14px;display:flex;gap:3px}
.gallery .arrows span{width:16px;height:16px;background:#555}
.gallery .photo{position:absolute;left:18px;top:50px;width:152px;height:219px;background:linear-gradient(#f3efea,#c8a78a 40%,#2c2a2a 75%,#1a1a1a)}

/* footer */
.footer{left:0;top:1122px;width:990px;height:78px;background:#f0f0f0;border-top:4px solid var(--pink)}
.footer-dot{left:166px;top:1150px;width:32px;height:32px;border-radius:50%;background:#d2d2d2}
.footer-links{left:212px;top:1152px;font-size:8px;color:#999}
.footer-copy{left:212px;top:1172px;font-size:8px;color:#444}
</style>
</head>
<body>

<header class="site-header abs"></header>
<div class="brand abs"><span class="brand-dot"></span>ellavida.example</div>
<div class="btn-social abs">Connect To Chatterly</div>
<div class="btn-login abs">LOGIN</div>
<div class="search abs">Enter Your Keywords Here...
  <span class="search-btn abs"><svg width="21" height="20" viewBox="0 0 21 20"><circle cx="9.5" cy="9" r="3.5" fill="none" stroke="#fff" stroke-width="1.6"/><line x1="12" y1="11.5" x2="15" y2="14.5" stroke="#fff" stroke-width="1.8"/></svg></span>
</div>

<nav class="main-nav abs">
  <ul>
    <li>LOVE &amp; SEX</li><li>ASTROLOGY</li><li>BEAUTY &amp; FASHION</li><li>LIFE STYLE</li><li>ENTERTAINMENT</li><li>BLOG</li><li>FOOD &amp; RECIPES</li><li>ARTICLES</li>
  </ul>
</nav>

<section class="hero abs"></section>
<div class="hero-photo abs" role="img" aria-label="Model wearing a mint green dress"></div>
<div class="hero-copy abs heading">
  <div class="kicker">AWESOME</div>
  <div class="title">MINT DRESSES</div>
  <div class="sub">COLLECTIONS</div>
  <p>Lorem ipsum dolor sit amet, consectetuer adipiscing elit, sed diam nonummy nibh euismod tincidunt...</p>
  <span class="btn-discover">DISCOVER NOW!</span>
</div>

<aside class="date-panel abs">
  <div class="date heading">May<b>07</b><small>,2013</small></div>
  <div class="teaser" style="height:57px"><h3>Want To Stay Slim?</h3><p>Lorem ipsum dolor sit amet, consectetuer adipiscing elit...</p></div>
  <div class="teaser" style="height:73px"><h3>Why Do Your Knees Hurt<br>When Running</h3><p>Lorem ipsum dolor sit amet,<br>consectetuer adipiscing elit...</p></div>
  <div class="teaser" style="height:73px"><h3>HAVE WE EVOLVED SEXUALLY?</h3><p>Lorem ipsum dolor sit amet,<br>consectetuer adipiscing elit, sed diam<br>nonummy nibh euis....</p></div>
  <div class="teaser" style="border:none"><h3>THE "PURR" OF CATS IS GOOD...</h3><p>Lorem ipsum dolor sit amet,<br>consectetuer adipiscing elit, sed diam<br>nonummy nibh euismod tincidunt.</p></div>
</aside>

<article class="feature box abs">
  <h2><span class="badge">20</span> Full Control of Wrinkles</h2>
  <p>Lorem ipsum dolor sit amet, consectetuer adipiscing elit, sed diam nonummy nibh euismod tincidunt ut laoreet dolore magna aliquam erat volutpat. Ut wisi enim ad minim veniam, quis nostrud exerci tation ullamcorper suscipit lobortis nisl ut aliquip ex ea commodo consequat. Duis autem vel eum iriure dolor in hendrerit in vulputate velit esse molestie...</p>
  <div class="meta">February 11, 2013 by Marisol Avery Ruiz</div>
</article>

<div class="register box abs">
  <div class="panel-title" style="border:none">REGISTER NOW!</div>
  <div class="field">Enter Your Email Address</div>
  <div class="btn-register">REGISTER!</div>
</div>

<article class="card box abs" style="left:166px">
  <div class="photo" role="img" aria-label="Woman holding a cat and a puppy" style="background:linear-gradient(135deg,#6b5a4a,#c9a585 50%,#8a7a66)"></div>
  <h3><span class="badge">32</span> Pet Owners</h3>
  <p>Lorem ipsum dolor sit amet, consectetuer adipiscing elit, sed diam nonummy nibh euismod tincidunt ut laoreet dolore magna aliquam erat volutpat.</p>
  <div class="meta">February 10, 2013 by Marisol Avery</div>
</article>
<article class="card box abs" style="left:329px">
  <div class="photo" role="img" aria-label="Mother hugging her young daughter" style="background:linear-gradient(135deg,#f4e9e6,#d9a58c 50%,#e9b3c8)"></div>
  <h3><span class="badge">29</span> Mothers</h3>
  <p>Lorem ipsum dolor sit amet, consectetuer adipiscing elit, sed diam nonummy nibh euismod tincidunt ut laoreet dolore magna aliquam erat volutpat.</p>
  <div class="meta">February 10, 2013 by Marisol Avery</div>
</article>
<article class="card box abs" style="left:491px">
  <div class="photo" role="img" aria-label="Smiling couple close together" style="border-color:var(--red);background:linear-gradient(135deg,#f1dcc4,#c99573 50%,#3a2d28)"></div>
  <h3><span class="badge">12</span> Lovers</h3>
  <p>Lorem ipsum dolor sit amet, consectetuer adipiscing elit, sed diam nonummy nibh euismod tincidunt ut laoreet dolore magna aliquam erat volutpat.</p>
  <div class="meta">February 10, 2013 by Marisol Avery</div>
</article>

<aside class="highlights box abs">
  <div class="panel-title">HIGHLIGHTS</div>
  <div class="hl-item"><span class="hl-num">01</span><div><b>Lorem ipsum dolor sit amet</b><span>consectetuer adipiscing elit...</span></div></div>
  <div class="hl-item"><span class="hl-num">02</span><div><b>Lorem ipsum dolor sit amet</b><span>consectetuer adipiscing elit...</span></div></div>
  <div class="hl-item"><span class="hl-num">03</span><div><b>Lorem ipsum dolor sit amet</b><span>consectetuer adipiscing elit...</span></div></div>
  <div class="hl-item"><span class="hl-num">04</span><div><b>Lorem ipsum dolor sit amet</b><span>consectetuer adipiscing elit...</span></div></div>
  <div class="hl-more">Get More Details...</div>
</aside>

<div class="promo abs">
  <span class="pct heading">25<small>%</small></span>
  <span class="line">The latest collection of <em>Awesome Orange Dress</em></span>
  <svg class="abs" style="right:0;top:0" width="42" height="37" viewBox="0 0 42 37"><polygon points="0,0 42,0 42,37" fill="#2b2b2b"/><polygon points="24,3 36,3 36,15" fill="#fff"/></svg>
</div>

<section class="popular box abs">
  <div class="panel-title"><span class="badge">20</span>MOST POPULAR</div>
  <div class="pop-item">
    <div class="pop-thumb" role="img" aria-label="Portrait of a brunette woman" style="background:linear-gradient(#f6f1ee,#6a4535 60%,#3a2a24)"></div>
    <div><h4>Lorem ipsum dolor sit amet, consectetuer adipiscing elit,</h4><p>Lorem ipsum dolor sit amet, consectetuer adipiscing elit, sed diam nonummy nibh euismod tincidunt ut laoreet dolore magna aliquam erat volutpat.</p><span class="btn-more">More Details...</span></div>
  </div>
  <div class="pop-item">
    <div class="pop-thumb" role="img" aria-label="Portrait of a blonde woman" style="background:linear-gradient(#f6f3ee,#d8bd8c 55%,#555)"></div>
    <div><h4>Lorem ipsum dolor sit amet, consectetuer adipiscing elit,</h4><p>Lorem ipsum dolor sit amet, consectetuer adipiscing elit, sed diam nonummy nibh euismod tincidunt ut laoreet dolore magna aliquam erat volutpat.</p><span class="btn-more">More Details...</span></div>
  </div>
</section>

<aside class="gallery box abs">
  <div class="panel-title">GALLERY</div>
  <div class="arrows">
    <span><svg width="16" height="16" viewBox="0 0 16 16"><polygon points="10,4 10,12 5,8" fill="#fff"/></svg></span>
    <span><svg width="16" height="16" viewBox="0 0 16 16"><polygon points="6,4 6,12 11,8" fill="#fff"/></svg></span>
  </div>
  <div class="photo" role="img" aria-label="Woman in a black lace blouse"></div>
</aside>

<footer class="footer abs"></footer>
<div class="footer-dot abs"></div>
<div class="footer-links abs">Home - Love &amp; Sex - Astrology - Beauty &amp; Fashion - Life Style - Entertainment - Blog - Blog - Food &amp; Recipes - Articles - Contact Us</div>
<div class="footer-copy abs">2013 ellavida.example Privacy Policy - Terms of Conditions. All Rights Reserved</div>

</body>
</html>
```